Business Cards

Business card design for my company.
I would like the card's background colour to be black. You can also see our web site to get an idea of our brand. https://www.dlqmarrowfield.com.au/
- Name
- Email

```html
<!DOCTYPE html>
<html lang="en">
<head>
<meta charset="utf-8">
<title>DLQ Marrowfield – Business Cards</title>
<link rel="stylesheet" href="https://fonts.googleapis.com/css2?family=Montserrat:wght@400;700&display=swap">
<style>
  :root {
    --stage: #e6e6e6;
    --card: #000000;
    --green: #14954a;
    --white: #f4f5f7;
    --text: #ffffff;
  }
  * { margin: 0; padding: 0; box-sizing: border-box; }
  html, body {
    width: 1200px;
    height: 1200px;
    overflow: hidden;
    background: var(--stage);
    font-family: "Montserrat", Arial, sans-serif;
  }
  .sheet { position: relative; width: 1200px; height: 1200px; }
  .card {
    position: absolute;
    left: 171px;
    width: 858px;
    height: 500px;
    background: var(--card);
    overflow: hidden;
  }
  .card--front { top: 82px; }
  .card--back { top: 615px; }
  .card__shapes {
    position: absolute;
    inset: 0;
    width: 100%;
    height: 100%;
  }
  .shape--white { fill: var(--white); }
  .shape--green { fill: var(--green); }

  .brand {
    position: absolute;
    display: flex;
    align-items: center;
    gap: 10px;
    color: var(--text);
    font-weight: 700;
    letter-spacing: 0.05em;
    white-space: nowrap;
  }
  .brand__mark {
    width: 16px;
    height: 16px;
    background: var(--green);
    flex: none;
  }
  .card--front .brand { left: 540px; top: 130px; font-size: 21px; }
  .card--back .brand { left: 101px; top: 155px; font-size: 26px; }
  .card--back .brand__mark { width: 20px; height: 20px; }

  .holder-name {
    position: absolute;
    left: 64px;
    top: 235px;
    font-size: 27px;
    font-weight: 700;
    color: var(--text);
    letter-spacing: 0.01em;
  }
  .contact-list {
    position: absolute;
    left: 64px;
    top: 336px;
    list-style: none;
  }
  .contact-list__item {
    display: flex;
    align-items: center;
    height: 39px;
    font-size: 22px;
    color: var(--text);
  }
  .contact-list__icon {
    width: 24px;
    height: 24px;
    margin-right: 20px;
    fill: var(--green);
    flex: none;
  }
</style>
</head>
<body>
<main class="sheet">

  <section class="card card--front" aria-label="Business card front">
    <svg class="card__shapes" viewBox="0 0 686 400" preserveAspectRatio="none" aria-hidden="true">
      <polygon class="shape--white" points="125,139 353,139 425,239 328,239"/>
      <polygon class="shape--green" points="0,173 303,173 343,219 686,219 686,232 0,232"/>
    </svg>

    <div class="brand"><span class="brand__mark"></span>DLQ MARROWFIELD</div>

    <h1 class="holder-name">SELIN AYDEMIR</h1>

    <ul class="contact-list">
      <li class="contact-list__item">
        <svg class="contact-list__icon" viewBox="0 0 24 24" aria-hidden="true"><path d="M6.6 10.8a15.1 15.1 0 0 0 6.6 6.6l2.2-2.2a1 1 0 0 1 1-.25 11.4 11.4 0 0 0 3.6.57 1 1 0 0 1 1 1V20a1 1 0 0 1-1 1A17 17 0 0 1 3 4a1 1 0 0 1 1-1h3.5a1 1 0 0 1 1 1c0 1.25.2 2.45.57 3.57a1 1 0 0 1-.25 1z"/></svg>
        0400 555 182
      </li>
      <li class="contact-list__item">
        <svg class="contact-list__icon" viewBox="0 0 24 24" aria-hidden="true"><path d="M2 5h20v14H2z M3 6.5v1l9 6 9-6v-1z" fill-rule="evenodd"/></svg>
        info@dlqmarrowfield.com.au
      </li>
      <li class="contact-list__item">
        <svg class="contact-list__icon" viewBox="0 0 24 24" aria-hidden="true"><path d="M12 2a10 10 0 1 0 0 20 10 10 0 0 0 0-20zm0 2c.9 0 2.2 1.9 2.7 5H9.3C9.8 5.9 11.1 4 12 4zM4.3 11h3a17 17 0 0 0 0 2h-3a8 8 0 0 1 0-2zm5 0h5.4a15 15 0 0 1 0 2H9.3a15 15 0 0 1 0-2zm7.4 0h3a8 8 0 0 1 0 2h-3a17 17 0 0 0 0-2zM9.3 15h5.4c-.5 3.1-1.8 5-2.7 5s-2.2-1.9-2.7-5z"/></svg>
        www.dlqmarrowfield.com.au
      </li>
    </ul>
  </section>

  <section class="card card--back" aria-label="Business card back">
    <svg class="card__shapes" viewBox="0 0 686 400" preserveAspectRatio="none" aria-hidden="true">
      <polygon class="shape--white" points="285,255 383,255 585,357 360,357"/>
      <polygon class="shape--green" points="308,277 686,277 686,338 463,338 425,292 318,292" stroke="#000" stroke-width="3"/>
    </svg>

    <div class="brand"><span class="brand__mark"></span>DLQ MARROWFIELD</div>
  </section>

</main>
</body>
</html>
```